Business card for our start up Automotive Shop

Clean business card design for our new automotive shop Brightline Motor Works. This card will be the template for all of our staff member including technicians and service advisors.

Brightline Motor Works is an automotive service shop catering to US domestic and asian import vehicles. We are a service and maintenance full service facility. Our aim is to provide the best quality workmanship and the best customer service experience in our industry.

Our target market are young professionals to people with families. We are not targeting a younger audience or the car modification scene. The card should be appealing to women of the 30+ age demographic.

We are a shop of younger professionals instead of an older crowd. The card design should reflect as such.

Target Market(s)

30+ Female demographic and 30+ male.

Industry/Entity Type

Automotive

Contact Information for Business Card

Must be clean and appealing to clients. Large enough and easy to read print.

Font styles to use
Sans Serif

Colors
f78f20
ffffff
b2b2b2
dddddd

Requirements
Must have
• Address, website and phone number
• 42-15 58th Ave
• Cedar Hollow NY 11462
• (718) 402-3917
• brightlinemotorworks.com
• There must be an area to add a Name and e-mail address for personalization purposes.
Nice to have
• Back of the card should have website.
• I would also like to incorporate yelp, google+, Facebook, and instagram widgets. Will add the exact pages but everything can be @ or / brightlinemotorworks
• That can be added on the back of the card.

```html
<!DOCTYPE html>
<html lang="en">
<head>
<meta charset="utf-8">
<title>Brightline Motor Works – Business Card</title>
<link rel="stylesheet" href="https://fonts.googleapis.com/css2?family=Open+Sans:wght@400;600;700&display=swap">
<style>
  :root {
    --brand-orange: #f78f20;
    --white: #ffffff;
    --mid-grey: #b2b2b2;
    --light-grey: #dddddd;
    --backdrop: #eeeeee;
    --card-shadow: rgba(0, 0, 0, 0.12);
  }
  * { margin: 0; padding: 0; box-sizing: border-box; }
  html, body {
    width: 1200px;
    height: 900px;
    overflow: hidden;
    background: var(--backdrop);
    font-family: "Open Sans", Arial, sans-serif;
  }
  .canvas {
    position: relative;
    width: 1200px;
    height: 900px;
  }
  .card {
    position: absolute;
    overflow: hidden;
    box-shadow: 0 4px 18px var(--card-shadow);
  }

  /* Front */
  .card-front {
    left: 77px;
    top: 35px;
    width: 588px;
    height: 362px;
    background: var(--brand-orange);
    color: var(--white);
  }
  .front-disc {
    position: absolute;
    left: 268px;
    top: 26px;
    width: 310px;
    height: 310px;
    border-radius: 50%;
    background: var(--white);
  }
  .person-name {
    position: absolute;
    left: 21px;
    top: 35px;
    font-size: 18px;
    font-weight: 700;
    letter-spacing: 0.3px;
  }
  .person-role {
    position: absolute;
    left: 21px;
    top: 58px;
    font-size: 14.5px;
    font-weight: 400;
  }
  .address {
    position: absolute;
    left: 21px;
    top: 99px;
    font-size: 15px;
    line-height: 21px;
  }
  .info-list {
    position: absolute;
    left: 22px;
    list-style: none;
    font-size: 15px;
  }
  .info-list li {
    display: flex;
    align-items: center;
    gap: 8px;
  }
  .social-list { top: 155px; }
  .social-list li { height: 25.5px; }
  .social-dot {
    width: 18px;
    height: 18px;
    border-radius: 50%;
    background: var(--white);
    flex: none;
  }
  .contact-list { top: 269px; }
  .contact-list li { height: 22px; }
  .contact-icon {
    width: 12px;
    height: 12px;
    flex: none;
    margin-right: 2px;
  }

  /* Back */
  .card-back {
    left: 388px;
    top: 505px;
    width: 567px;
    height: 352px;
    background: var(--white);
  }
  .brand-lockup {
    position: absolute;
    left: 72px;
    top: 125px;
    display: flex;
    align-items: center;
  }
  .brand-disc {
    width: 98px;
    height: 98px;
    border-radius: 50%;
    background: var(--brand-orange);
    flex: none;
  }
  .brand-divider {
    width: 3px;
    height: 98px;
    background: var(--mid-grey);
    margin: 0 12px 0 12px;
  }
  .brand-name {
    color: var(--brand-orange);
    font-weight: 600;
    line-height: 1;
  }
  .brand-name .line-1 {
    display: block;
    font-size: 33px;
    letter-spacing: 1px;
  }
  .brand-name .line-2 {
    display: block;
    font-size: 20px;
    letter-spacing: 6.5px;
    margin-top: 10px;
  }
</style>
</head>
<body>
<main class="canvas">

  <section class="card card-front" aria-label="Business card front">
    <div class="front-disc"></div>

    <h1 class="person-name">DANIEL REYES</h1>
    <p class="person-role">Managing Director</p>

    <address class="address">
      42-15 58th Ave<br>
      Cedar Hollow NY 11462
    </address>

    <ul class="info-list social-list">
      <li><span class="social-dot"></span>@brightlinemotorworks</li>
      <li><span class="social-dot"></span>@brightlinemotorworks</li>
      <li><span class="social-dot"></span>@brightlinemotorworks</li>
    </ul>

    <ul class="info-list contact-list">
      <li>
        <svg class="contact-icon" viewBox="0 0 24 24" aria-hidden="true">
          <path fill="#ffffff" d="M6.6 10.8a15.1 15.1 0 0 0 6.6 6.6l2.2-2.2a1 1 0 0 1 1-.25 11.4 11.4 0 0 0 3.6.57 1 1 0 0 1 1 1V20a1 1 0 0 1-1 1A17 17 0 0 1 3 4a1 1 0 0 1 1-1h3.5a1 1 0 0 1 1 1c0 1.25.2 2.45.57 3.57a1 1 0 0 1-.25 1z"/>
        </svg>
        (718) 402-3917
      </li>
      <li>
        <svg class="contact-icon" viewBox="0 0 24 24" aria-hidden="true">
          <path fill="#ffffff" d="M2 5h20v14H2z"/>
          <path fill="none" stroke="#f78f20" stroke-width="2" d="M3 6l9 7 9-7"/>
        </svg>
        info@brightlinemotorworks.com
      </li>
      <li>
        <svg class="contact-icon" viewBox="0 0 24 24" aria-hidden="true">
          <circle cx="12" cy="12" r="10" fill="#ffffff"/>
          <path fill="none" stroke="#f78f20" stroke-width="1.6" d="M2 12h20M12 2c3 3 3 17 0 20M12 2c-3 3-3 17 0 20"/>
        </svg>
        www.brightlinemotorworks.com
      </li>
    </ul>
  </section>

  <section class="card card-back" aria-label="Business card back">
    <div class="brand-lockup">
      <span class="brand-disc"></span>
      <span class="brand-divider"></span>
      <p class="brand-name">
        <span class="line-1">BRIGHTLINE</span>
        <span class="line-2">MOTOR WORKS</span>
      </p>
    </div>
  </section>

</main>
</body>
</html>
```